Harbourline Refrigeration business card design

We would like a new design for our business card as we have a new logo.
We need generic business card to give our customers with our office details - with the option of making it individualized for each manager

Target Market(s)

Companies and homeowners

Industry/Entity Type

Air Conditioning

Contact Information for Business Card

We are not sure if we want single or double sided it will depend on the design we choose

Colors
33a6d7
0255a3

Requirements
Must have
• Logo
• phone: (08) 8721 5940
• email: harbourserve@tealnet.example
• website: www.harbourlinerefrigeration.example
• AU61420
• BLD472913
Nice to have
• Address - Shed 5/284 Tallis Rd, Kestrel Bay SA 5990

```html
<!DOCTYPE html>
<html lang="en">
<head>
<meta charset="utf-8">
<title>Harbourline Refrigeration – Business Card</title>
<link href="https://fonts.googleapis.com/css2?family=Arimo:wght@400;700&display=swap" rel="stylesheet">
<style>
  :root {
    --brand-navy: #0255a3;
    --brand-deep: #00437f;
    --brand-sky: #33a6d7;
    --ink: #1a1a1a;
    --band-start: #064c78;
    --band-mid: #8c9dbd;
    --card-edge: #7a7a7a;
    --paper: #ffffff;
  }
  * { box-sizing: border-box; margin: 0; padding: 0; }
  html, body {
    width: 1200px; height: 1189px; overflow: hidden;
    background: var(--paper);
    font-family: "Arimo", Arial, sans-serif;
    color: var(--ink);
  }
  .sheet { position: relative; width: 1200px; height: 1189px; }
  .card {
    position: absolute; left: 157px; width: 882px; height: 533px;
    border: 1px solid var(--card-edge);
    background: var(--paper); overflow: hidden;
  }
  .card--front { top: 45px; }
  .card--back { top: 619px; }

  .front-brand {
    position: absolute; left: 56px; top: 112px;
    display: flex; align-items: center; gap: 14px;
    color: var(--brand-deep); font-weight: 700; line-height: 1.05;
  }
  .brand-dot {
    width: 26px; height: 26px; border-radius: 50%;
    background: var(--brand-sky); flex: none;
  }
  .front-brand .name { display: block; font-size: 50px; letter-spacing: -0.5px; }
  .front-brand .name-sub { display: block; font-size: 24px; }

  .contact { position: absolute; left: 428px; top: 194px; font-size: 26px; line-height: 1; }
  .contact-row { display: flex; align-items: center; gap: 10px; height: 38px; }
  .contact-row svg { width: 34px; height: 26px; flex: none; }
  .website {
    position: absolute; right: 22px; top: 276px;
    font-size: 21px; white-space: nowrap;
  }
  .licence {
    position: absolute; left: 560px; width: 132px; text-align: center;
    font-size: 24px;
  }
  .licence--au { top: 328px; }
  .licence--bld { top: 374px; }

  .address-band {
    position: absolute; left: 0; top: 427px; width: 100%; height: 106px;
    background: linear-gradient(90deg, var(--band-start) 0%, #4c6a92 22%, var(--band-mid) 45%, #b9c2d8 70%, var(--paper) 98%);
    color: var(--paper); font-size: 33px; line-height: 46px;
    padding: 12px 0 0 54px;
  }
  .address-band p:last-child { margin-left: -6px; }

  .back-brand {
    position: absolute; left: 0; top: 0; width: 100%; height: 100%;
    display: flex; flex-direction: column; align-items: center; justify-content: center;
    color: var(--brand-deep); font-weight: 700; line-height: 1.05; text-align: center;
    padding-top: 90px;
  }
  .back-brand .brand-dot { width: 44px; height: 44px; margin-bottom: 26px; }
  .back-brand .name { font-size: 92px; letter-spacing: -1px; }
  .back-brand .name-sub { font-size: 44px; }
</style>
</head>
<body>
<main class="sheet">
  <section class="card card--front" aria-label="Card front">
    <div class="front-brand">
      <span class="brand-dot"></span>
      <div>
        <span class="name">Harbourline</span>
        <span class="name-sub">Refrigeration</span>
      </div>
    </div>

    <div class="contact">
      <div class="contact-row">
        <svg viewBox="0 0 34 26" aria-hidden="true"><rect x="1" y="1" width="32" height="24" fill="none" stroke="#333" stroke-width="1.5"/><path d="M1 1 L17 15 L33 1 M1 25 L13 12 M33 25 L21 12" fill="none" stroke="#333" stroke-width="1.5"/></svg>
        <span>harbourserve@tealnet.example</span>
      </div>
      <div class="contact-row">
        <svg viewBox="0 0 34 26" aria-hidden="true"><path d="M2 9 Q17 0 32 9 L29 12 L24 10 L24 7 Q17 5 10 7 L10 10 L5 12 Z" fill="none" stroke="#333" stroke-width="1.4"/><path d="M9 12 L25 12 L29 24 L5 24 Z" fill="none" stroke="#333" stroke-width="1.4"/><circle cx="17" cy="18" r="3.5" fill="none" stroke="#333" stroke-width="1.4"/></svg>
        <span>(08) 8721 5940</span>
      </div>
    </div>
    <div class="website">website: www.harbourlinerefrigeration.example</div>
    <div class="licence licence--au">AU61420</div>
    <div class="licence licence--bld">BLD472913</div>

    <div class="address-band">
      <p>Shed 5/284 Tallis Rd,</p>
      <p>Kestrel Bay SA 5990</p>
    </div>
  </section>

  <section class="card card--back" aria-label="Card back">
    <div class="back-brand">
      <span class="brand-dot"></span>
      <span class="name">Harbourline</span>
      <span class="name-sub">Refrigeration</span>
    </div>
  </section>
</main>
</body>
</html>
```